Update Theme for existing site

Update Theme and allow for integration of product update sheets
Updates

Please use the existing website brivolanetco.com for content. Would like a new homepage and ability to update products, ideally by placing PDF files in a set directory location. The current theme is an old wordpress, but we have had problems updating it. A similar company to ours would be: dermuth-works.com Wendrix.io to get an idea of what we would like.

Coding

```html
<!DOCTYPE html>
<html lang="en">
<head>
<meta charset="utf-8">
<title>Brivolanet Resource – Homepage Proposal</title>
<link rel="stylesheet" href="https://fonts.googleapis.com/css2?family=Montserrat:wght@300;400;500&family=Roboto:wght@400;500&family=Source+Sans+3:wght@400;700;900&display=swap">
<style>
  :root {
    --navy-deep: #0c0f2e;
    --navy: #1b2470;
    --violet: #5a3fa8;
    --sky: #00aeef;
    --accent: #1fb3f0;
    --white: #ffffff;
    --ink: #0a0a0a;
    --card-line: #eef1f4;
  }
  * { margin: 0; padding: 0; box-sizing: border-box; }
  html, body { width: 960px; height: 1200px; overflow: hidden; background: var(--white); }
  body { position: relative; font-family: "Source Sans 3", sans-serif; }

  .site-screen {
    position: absolute; left: 20px; top: 20px; width: 920px; height: 516px;
    overflow: hidden; background: var(--white);
  }
  .hero {
    position: absolute; inset: 0 0 76px 0;
    background: radial-gradient(ellipse at 20% 90%, #7c4fb8 0%, transparent 45%),
                linear-gradient(160deg, var(--navy-deep) 0%, var(--navy) 55%, var(--violet) 100%);
  }
  .hero-visual {
    position: absolute; right: 0; top: 0; width: 450px; height: 100%;
    background: linear-gradient(135deg, #8da4d6 0%, #5a6fa8 45%, #2c3a78 100%);
    opacity: 0.85;
  }
  .site-nav {
    position: absolute; top: 14px; left: 108px; right: 120px;
    display: flex; align-items: center; justify-content: space-between;
  }
  .brand { display: flex; align-items: center; gap: 6px; font-family: "Montserrat", sans-serif; font-size: 16px; font-weight: 400; color: var(--accent); }
  .brand-mark { width: 14px; height: 14px; background: var(--accent); }
  .nav-links { display: flex; gap: 24px; list-style: none; font-family: "Roboto", sans-serif; font-size: 10px; color: var(--white); }
  .nav-links .is-active, .nav-links .is-highlight { color: var(--accent); }

  .hero-copy { position: absolute; left: 117px; top: 106px; width: 400px; color: var(--white); }
  .hero-kicker { font-family: "Montserrat", sans-serif; font-weight: 500; font-size: 30px; }
  .hero-title { font-family: "Montserrat", sans-serif; font-weight: 300; font-size: 58px; line-height: 1.1; margin-top: 4px; }
  .hero-text { font-family: "Roboto", sans-serif; font-size: 8.5px; line-height: 1.7; margin-top: 14px; }
  .btn-outline {
    display: inline-block; margin-top: 36px; padding: 6px 15px;
    border: 1px solid var(--accent); color: var(--accent);
    font-family: "Roboto", sans-serif; font-size: 9px; text-transform: uppercase;
  }

  .feature-strip { position: absolute; left: 0; right: 0; bottom: 0; height: 76px; background: var(--white); }
  .feature-card {
    position: absolute; top: 28px; width: 226px; height: 60px;
    border: 1px solid var(--card-line); background: var(--white);
  }
  .feature-card:nth-child(1) { left: 102px; }
  .feature-card:nth-child(2) { left: 346px; }
  .feature-card:nth-child(3) { left: 590px; }
  .feature-icon { position: absolute; left: 87px; top: 32px; width: 52px; height: 52px; border-radius: 50%; background: var(--sky); }

  .offer-panel {
    position: absolute; left: 70px; top: 536px; width: 820px; height: 664px;
    background: var(--sky); color: var(--white); padding: 56px 56px 0 56px;
  }
  .offer-label { font-size: 21px; font-weight: 700; }
  .demo-url { font-size: 46px; font-weight: 900; color: var(--ink); text-align: right; margin: 6px 10px 0 0; }
  .offer-note { font-size: 21px; line-height: 1.35; margin-top: 20px; }
  .offer-heading { font-size: 21px; font-weight: 700; margin-top: 44px; }
  .offer-list { list-style: none; font-size: 21px; line-height: 1.34; }
  .offer-signoff { font-size: 21px; color: var(--ink); text-align: right; margin: 44px 14px 0 0; }
</style>
</head>
<body>
  <section class="site-screen">
    <div class="hero">
      <div class="hero-visual" role="img" aria-label="Illustration of a large satellite with dish antenna and solar panels orbiting above Earth"></div>
      <header class="site-nav">
        <div class="brand"><span class="brand-mark"></span>Brivolanet Resource</div>
        <ul class="nav-links">
          <li class="is-active">Home</li><li>About</li><li>Services</li><li>Products</li><li class="is-highlight">News</li><li>Contact</li>
        </ul>
      </header>
      <div class="hero-copy">
        <p class="hero-kicker">A Driving Force</p>
        <h1 class="hero-title">in Satellites</h1>
        <p class="hero-text">Brivolanet's engineers possess a broad array of skills and experience, on spacecraft as small as CubeSats, to larger communications satellites like the Halvern Dynamics K400 series, to crewed spacecraft like Corvan, Sky Runner, Glider, and OSP.</p>
        <span class="btn-outline">Contact us</span>
      </div>
    </div>
    <div class="feature-strip">
      <div class="feature-card"><span class="feature-icon"></span></div>
      <div class="feature-card"><span class="feature-icon"></span></div>
      <div class="feature-card"><span class="feature-icon"></span></div>
    </div>
  </section>

  <section class="offer-panel">
    <p class="offer-label">Check this website in LIVE DEMO:</p>
    <p class="demo-url">demo6.pixelvane.online</p>
    <p class="offer-note">please note: As the deadline of the brief is very close, I made the sample preview. But I’m still working with the design, so you can see all changes online</p>
    <p class="offer-heading">Whats include to my offer:</p>
    <ol class="offer-list">
      <li>1. Responsive design</li>
      <li>2. Fully functional website with unlimited revisions (untill you be happy with it)</li>
      <li>3. Installation to your hosting</li>
      <li>4. Additional graphic designs required for this website</li>
      <li>5. Additional components and plugins (like: live chat, galleries, forms, pdf’s)</li>
      <li>6. Friendly support anytime</li>
    </ol>
    <p class="offer-signoff">Looking forward to your feedback</p>
  </section>
</body>
</html>
```